Web design for Marketplace

Guys!
1st of all, thank you for willing to help me out.
I have attached PDF file with examples.
I am looking for professional and clean design for my new project “ Lantern of Seers “. Its marketplace for Psychic Readers around the world. Where they will able to register to provide their services via Chat,Email and sell their products on their personal stores.
Customer will able to get services and buy products from Psychic on Marketplace.
url : http://www.lanternofseers-demo.net
Please note: it doesn’t matter, what my current site looks like. I am looking for completely new design.
It doesn't matter if you add or remove : Vidlume video or even text which is on the home page in new design.
Following are the main pages of the website, which i am looking to be design.
1. Home page
2. Psychic
3. Marketplace
4. Psychic profile page
5. Psychic Store page
6. Psychic product page
7. Logo
following is the website, which i like the most. I would love to have something like that. It is neat , clean and friendly. I am looking for depth in design and neatness and borders (matter and a lot and it should be prefect ).
http://www.craftnook-demo.net
P.S : i believe it will be helpful to choose one of you. If you can only create design of " Homepage" at 1st , so i can go ahead and hire one of you guys.
Best,
Hi guys!
Guys,

```html
<!DOCTYPE html>
<html lang="en">
<head>
<meta charset="utf-8">
<title>Lantern of Seers – Home</title>
<link rel="stylesheet" href="https://fonts.googleapis.com/css2?family=Open+Sans:wght@400;600;700&family=Montserrat:wght@400;500&family=Gelasio:ital@1&family=Oswald:wght@500&display=swap">
<style>
:root{
  --page-bg:#e9e9e9;
  --column-bg:#f4f4f4;
  --card-bg:#ffffff;
  --card-border:#dcdcdc;
  --ink:#333333;
  --ink-soft:#8a8a8a;
  --ink-quote:#9a9a9a;
  --accent-blue:#2a8fd0;
  --link-blue:#2f9fd8;
  --teal:#12b3d6;
  --nav-bg:#e3e3e3;
  --quote-orange:#f0a02a;
  --join-yellow:#f5b515;
  --join-yellow-dark:#e49a0a;
  --join-blue:#53bde6;
  --signup:#3aa6d0;
}
*{box-sizing:border-box;margin:0;padding:0}
html,body{width:1200px;height:2350px;overflow:hidden}
body{background:var(--page-bg);font-family:"Open Sans",Arial,sans-serif;color:var(--ink);position:relative}
a{text-decoration:none;color:inherit}

.site{position:absolute;left:140px;top:0;width:920px;height:2350px;background:var(--column-bg);box-shadow:0 0 18px rgba(0,0,0,.12)}

/* header */
.header{position:absolute;left:0;top:0;width:920px;height:110px;background:#fff}
.brand{position:absolute;left:20px;top:28px;width:160px;height:70px;display:flex;align-items:center;gap:8px}
.brand-mark{width:14px;height:14px;background:#c9302c;flex:none}
.brand-name{font-family:"Open Sans",sans-serif;font-weight:700;font-size:19px;line-height:22px;color:#1d1d1d}
.account-links{position:absolute;left:200px;top:18px;font-size:13px;color:var(--link-blue)}
.account-links a{margin-right:14px}
.help-link{position:absolute;right:20px;top:18px;font-size:13px;color:var(--link-blue)}
.nav{position:absolute;left:200px;top:50px;width:700px;height:46px;background:var(--nav-bg);border:1px solid #d3d3d3;border-radius:3px;display:flex;align-items:center;padding-left:6px}
.nav-item{font-size:14px;color:var(--link-blue);padding:0 14px;border-right:1px solid #cfcfcf;line-height:26px}
.nav-item:last-of-type{border-right:none}
.search{position:absolute;left:300px;top:8px;width:306px;height:28px;background:#fff;border:1px solid #cfcfcf}
.search-button{position:absolute;left:612px;top:8px;width:78px;height:28px;background:linear-gradient(#fafafa,#dedede);border:1px solid #bdbdbd;border-radius:4px;font-size:13px;color:#444;text-align:center;line-height:26px}

/* hero */
.hero{position:absolute;left:20px;top:124px;width:882px;height:362px;background:linear-gradient(135deg,#b9c9d6 0%,#d7d2c8 35%,#9fb3c6 65%,#cfc6bb 100%)}
.hero-title{position:absolute;left:124px;top:142px;width:632px;height:78px;background:var(--accent-blue);border:3px solid rgba(255,255,255,.55);box-shadow:0 3px 10px rgba(0,0,0,.3);color:#fff;font-family:"Open Sans",sans-serif;font-weight:600;font-size:38px;text-align:center;line-height:72px}

/* top psychics */
.section-title{position:absolute;font-family:"Open Sans",sans-serif;font-weight:600;font-size:17px;color:var(--accent-blue)}
.top-title{left:12px;top:516px}
.psychic-grid{position:absolute;left:12px;top:566px;display:grid;grid-template-columns:repeat(3,286px);grid-auto-rows:238px;column-gap:20px;row-gap:18px}
.psychic-card{position:relative;background:var(--card-bg);border:1px solid var(--card-border);box-shadow:0 1px 3px rgba(0,0,0,.08)}
.psychic-photo{position:absolute;left:12px;top:12px;width:80px;height:80px;background:linear-gradient(160deg,#d9c4b1,#8d7562)}
.psychic-name{position:absolute;left:100px;top:56px;font-family:"Montserrat",sans-serif;font-weight:500;font-size:17px;color:#3a3a3a}
.psychic-role{position:absolute;left:100px;top:78px;font-size:10px;color:var(--ink-soft)}
.psychic-quote{position:absolute;left:14px;top:106px;width:256px;font-family:"Gelasio",Georgia,serif;font-style:italic;font-size:13px;line-height:19.5px;color:var(--ink-quote)}
.q-open,.q-close{font-family:Georgia,serif;font-style:normal;font-weight:700;font-size:26px;line-height:0;color:var(--quote-orange);vertical-align:-8px}
.q-open{margin-right:4px}
.q-close{margin-left:4px}
.read-more{position:absolute;right:14px;bottom:14px;font-size:11px;color:var(--link-blue)}

/* newsletter */
.newsletter{position:absolute;left:12px;top:1612px;width:188px;height:224px;background:#fff;border:1px solid #e2e2e2;padding:12px 12px}
.newsletter h3{font-family:"Open Sans",sans-serif;font-weight:600;font-size:15px;color:#333;padding-bottom:6px;border-bottom:1px solid #ddd;margin-bottom:10px}
.newsletter p{font-size:12px;line-height:15px;color:#666}
.email-field{margin-top:16px;height:30px;border:1px solid #bbb;font-size:12px;color:#444;padding:6px 8px}
.signup{display:inline-block;margin-top:12px;width:88px;height:30px;background:var(--signup);border-radius:4px;color:#fff;font-weight:700;font-size:15px;text-align:center;line-height:30px}
.newsletter .other{display:block;margin-top:8px;font-size:12px;color:var(--link-blue)}

.market-title{left:216px;top:1616px}
.market-grid{position:absolute;left:216px;top:1664px;display:grid;grid-template-columns:repeat(8,74px);grid-auto-rows:74px;gap:20px 14px}
.product-thumb{border:2px solid #fff;box-shadow:0 1px 3px rgba(0,0,0,.25)}

/* join banner */
.join-rule{position:absolute;left:0;top:1910px;width:920px;height:1px;background:linear-gradient(90deg,transparent,#cfcfcf 20%,#cfcfcf 80%,transparent)}
.join-banner{position:absolute;left:204px;top:1884px;width:512px;height:56px;display:flex;border-radius:4px;overflow:hidden;box-shadow:0 2px 4px rgba(0,0,0,.25)}
.join-ask{width:346px;background:linear-gradient(var(--join-yellow),var(--join-yellow-dark));color:#fff;font-family:"Oswald",sans-serif;font-weight:500;font-size:32px;text-align:center;line-height:56px;letter-spacing:.5px}
.join-now{flex:1;background:linear-gradient(#7fd0ef,var(--join-blue));color:#1f5f85;font-family:"Oswald",sans-serif;font-weight:500;font-size:30px;display:flex;align-items:center;justify-content:center;gap:8px}

/* video */
.video-frame{position:absolute;left:20px;top:1986px;width:406px;height:244px;background:#fff;border:1px solid #dcdcdc;box-shadow:0 1px 6px rgba(0,0,0,.15);padding:20px 18px}
.video-still{width:368px;height:178px;background:linear-gradient(135deg,#5a5046,#a8927a 55%,#3d3a36)}
.video-bar{width:368px;height:12px;background:#1b1b1b}
.video-brand{position:absolute;left:460px;top:1994px;display:flex;align-items:center;gap:10px}
.video-brand .brand-word{font-family:"Open Sans",sans-serif;font-weight:600;font-size:30px;color:#333}
.video-brand .brand-label{font-family:"Open Sans",sans-serif;font-weight:400;font-size:26px;color:#444}
.video-brand .brand-square{width:16px;height:16px;background:#d9302a}
.video-heading{position:absolute;left:460px;top:2062px;width:440px;font-family:"Open Sans",sans-serif;font-weight:600;font-size:27px;line-height:34px;color:#555}
.video-text{position:absolute;left:460px;top:2140px;width:440px;font-size:13.5px;line-height:19px;color:#555}
.video-more{position:absolute;left:460px;top:2214px;font-size:12px;color:var(--link-blue)}

/* footer */
.footer{position:absolute;left:0;top:2266px;width:920px;height:84px;background:var(--teal);color:#fff;padding:20px 20px}
.footer-links a{font-size:12px;margin-right:16px}
.footer-legal{margin-top:16px;font-size:11.5px}
</style>
</head>
<body>
<div class="site">
  <header class="header">
    <a class="brand" href="http://www.lanternofseers-demo.net"><span class="brand-mark"></span><span class="brand-name">Lantern of Seers</span></a>
    <nav class="account-links"><a href="#">Login</a><a href="#">Signup</a></nav>
    <a class="help-link" href="#">Help</a>
    <div class="nav">
      <a class="nav-item" href="#">Psychic</a>
      <a class="nav-item" href="#">Marketplace</a>
      <a class="nav-item" href="#">My account</a>
      <div class="search"></div>
      <div class="search-button">Search</div>
    </div>
  </header>

  <section class="hero" role="img" aria-label="Crowd of smiling people each holding up a white frame around their face">
    <h1 class="hero-title">Meet Our Expert Psychic Seers</h1>
  </section>

  <h2 class="section-title top-title">Top Pyschics</h2>
  <div class="psychic-grid">
    <article class="psychic-card"><div class="psychic-photo" role="img" aria-label="Portrait of Dale Ferrin"></div><div class="psychic-name">Dale Ferrin</div><div class="psychic-role">Product Owner, Northway Insights</div><p class="psychic-quote"><span class="q-open">“</span>Lorem Ipsum. Proin gravida nibh vel velit auctor aliquet. Aenean sollicitudin, lorem quis bibendum auctor, nisi elit consequat ipsum, nec sagittis sem nibh id elit.<span class="q-close">”</span></p><a class="read-more" href="#">Read more</a></article>
    <article class="psychic-card"><div class="psychic-photo" role="img" aria-label="Portrait of Rick Lomasso"></div><div class="psychic-name">Rick Lomasso</div><div class="psychic-role">CEO and Founder</div><p class="psychic-quote"><span class="q-open">“</span>Lorem Ipsum. Proin gravida nibh vel velit auctor aliquet. Aenean sollicitudin, lorem quis bibendum auctor, nisi elit consequat ipsum, nec sagittis sem nibh id elit.<span class="q-close">”</span></p><a class="read-more" href="#">Read more</a></article>
    <article class="psychic-card"><div class="psychic-photo" role="img" aria-label="Portrait of Mohan"></div><div class="psychic-name">Mohan</div><div class="psychic-role">Product Owner, Northway Insights</div><p class="psychic-quote"><span class="q-open">“</span>Lorem Ipsum. Proin gravida nibh vel velit auctor aliquet. Aenean sollicitudin, lorem quis bibendum auctor, nisi elit consequat ipsum, nec sagittis sem nibh id elit.<span class="q-close">”</span></p><a class="read-more" href="#">Read more</a></article>
    <article class="psychic-card"><div class="psychic-photo" role="img" aria-label="Portrait of a psychic reader"></div><div class="psychic-name">Lorem Ipsum</div><div class="psychic-role">Product Owner, Northway Insights</div><p class="psychic-quote"><span class="q-open">“</span>Lorem Ipsum. Proin gravida nibh vel velit auctor aliquet. Aenean sollicitudin, lorem quis bibendum auctor, nisi elit consequat ipsum, nec sagittis sem nibh id elit.<span class="q-close">”</span></p><a class="read-more" href="#">Read more</a></article>
    <article class="psychic-card"><div class="psychic-photo" role="img" aria-label="Portrait of a psychic reader"></div><div class="psychic-name">Lorem Ipsum</div><div class="psychic-role">Product Owner, Northway Insights</div><p class="psychic-quote"><span class="q-open">“</span>Lorem Ipsum. Proin gravida nibh vel velit auctor aliquet. Aenean sollicitudin, lorem quis bibendum auctor, nisi elit consequat ipsum, nec sagittis sem nibh id elit.<span class="q-close">”</span></p><a class="read-more" href="#">Read more</a></article>
    <article class="psychic-card"><div class="psychic-photo" role="img" aria-label="Portrait of a psychic reader"></div><div class="psychic-name">Lorem Ipsum</div><div class="psychic-role">Product Owner, Northway Insights</div><p class="psychic-quote"><span class="q-open">“</span>Lorem Ipsum. Proin gravida nibh vel velit auctor aliquet. Aenean sollicitudin, lorem quis bibendum auctor, nisi elit consequat ipsum, nec sagittis sem nibh id elit.<span class="q-close">”</span></p><a class="read-more" href="#">Read more</a></article>
    <article class="psychic-card"><div class="psychic-photo" role="img" aria-label="Portrait of a psychic reader"></div><div class="psychic-name">Lorem Ipsum</div><div class="psychic-role">Product Owner, Northway Insights</div><p class="psychic-quote"><span class="q-open">“</span>Lorem Ipsum. Proin gravida nibh vel velit auctor aliquet. Aenean sollicitudin, lorem quis bibendum auctor, nisi elit consequat ipsum, nec sagittis sem nibh id elit.<span class="q-close">”</span></p><a class="read-more" href="#">Read more</a></article>
    <article class="psychic-card"><div class="psychic-photo" role="img" aria-label="Portrait of a psychic reader"></div><div class="psychic-name">Lorem Ipsum</div><div class="psychic-role">Product Owner, Northway Insights</div><p class="psychic-quote"><span class="q-open">“</span>Lorem Ipsum. Proin gravida nibh vel velit auctor aliquet. Aenean sollicitudin, lorem quis bibendum auctor, nisi elit consequat ipsum, nec sagittis sem nibh id elit.<span class="q-close">”</span></p><a class="read-more" href="#">Read more</a></article>
    <article class="psychic-card"><div class="psychic-photo" role="img" aria-label="Portrait of a psychic reader"></div><div class="psychic-name">Lorem Ipsum</div><div class="psychic-role">Product Owner, Northway Insights</div><p class="psychic-quote"><span class="q-open">“</span>Lorem Ipsum. Proin gravida nibh vel velit auctor aliquet. Aenean sollicitudin, lorem quis bibendum auctor, nisi elit consequat ipsum, nec sagittis sem nibh id elit.<span class="q-close">”</span></p><a class="read-more" href="#">Read more</a></article>
    <article class="psychic-card"><div class="psychic-photo" role="img" aria-label="Portrait of a psychic reader"></div><div class="psychic-name">Lorem Ipsum</div><div class="psychic-role">Product Owner, Northway Insights</div><p class="psychic-quote"><span class="q-open">“</span>Lorem Ipsum. Proin gravida nibh vel velit auctor aliquet. Aenean sollicitudin, lorem quis bibendum auctor, nisi elit consequat ipsum, nec sagittis sem nibh id elit.<span class="q-close">”</span></p><a class="read-more" href="#">Read more</a></article>
    <article class="psychic-card"><div class="psychic-photo" role="img" aria-label="Portrait of a psychic reader"></div><div class="psychic-name">Lorem Ipsum</div><div class="psychic-role">Product Owner, Northway Insights</div><p class="psychic-quote"><span class="q-open">“</span>Lorem Ipsum. Proin gravida nibh vel velit auctor aliquet. Aenean sollicitudin, lorem quis bibendum auctor, nisi elit consequat ipsum, nec sagittis sem nibh id elit.<span class="q-close">”</span></p><a class="read-more" href="#">Read more</a></article>
    <article class="psychic-card"><div class="psychic-photo" role="img" aria-label="Portrait of a psychic reader"></div><div class="psychic-name">Lorem Ipsum</div><div class="psychic-role">Product Owner, Northway Insights</div><p class="psychic-quote"><span class="q-open">“</span>Lorem Ipsum. Proin gravida nibh vel velit auctor aliquet. Aenean sollicitudin, lorem quis bibendum auctor, nisi elit consequat ipsum, nec sagittis sem nibh id elit.<span class="q-close">”</span></p><a class="read-more" href="#">Read more</a></article>
  </div>

  <aside class="newsletter">
    <h3>Daily Finds Email</h3>
    <p>Get gift ideas, editors' picks &amp; fresh trends in your inbox.</p>
    <div class="email-field">Enter your email</div>
    <a class="signup" href="#">Sign Up</a>
    <a class="other" href="#">See our other newsletters</a>
  </aside>

  <h2 class="section-title market-title">Psychic Marketplace</h2>
  <div class="market-grid">
    <div class="product-thumb" role="img" aria-label="Turquoise bead jewellery" style="background:linear-gradient(135deg,#7fd6d0,#3fa7a8)"></div>
    <div class="product-thumb" role="img" aria-label="Dark beaded bracelet" style="background:linear-gradient(135deg,#3a2f2c,#b5492d)"></div>
    <div class="product-thumb" role="img" aria-label="Pink and purple beads" style="background:linear-gradient(135deg,#d78ad0,#8c4aa8)"></div>
    <div class="product-thumb" role="img" aria-label="Colourful round beads" style="background:linear-gradient(135deg,#e65b8a,#f2c14a)"></div>
    <div class="product-thumb" role="img" aria-label="Blue glass pendant" style="background:linear-gradient(135deg,#c7d4e2,#2f5fa8)"></div>
    <div class="product-thumb" role="img" aria-label="Blue charm bead" style="background:linear-gradient(135deg,#8b8f95,#3b5c8a)"></div>
    <div class="product-thumb" role="img" aria-label="Teal glass charm" style="background:linear-gradient(135deg,#2b3a3d,#4bb2c4)"></div>
    <div class="product-thumb" role="img" aria-label="Silver charm on wood" style="background:linear-gradient(135deg,#6b5a4a,#cfc6b8)"></div>
    <div class="product-thumb" role="img" aria-label="Beaded strand" style="background:linear-gradient(135deg,#a9adb3,#2c3e5a)"></div>
    <div class="product-thumb" role="img" aria-label="Blue glass pendant" style="background:linear-gradient(135deg,#dfe6ee,#2b66b8)"></div>
    <div class="product-thumb" role="img" aria-label="Turquoise flower beads" style="background:linear-gradient(135deg,#3a2f2c,#5fc3c7)"></div>
    <div class="product-thumb" role="img" aria-label="Silver charm on wood" style="background:linear-gradient(135deg,#5c4a3c,#bfb6a8)"></div>
    <div class="product-thumb" role="img" aria-label="Turquoise bead jewellery" style="background:linear-gradient(135deg,#9ee0da,#45aab0)"></div>
    <div class="product-thumb" role="img" aria-label="Turquoise flower beads" style="background:linear-gradient(135deg,#2f2a28,#4dbcc4)"></div>
    <div class="product-thumb" role="img" aria-label="Colourful round beads" style="background:linear-gradient(135deg,#f0c040,#d9487a)"></div>
    <div class="product-thumb" role="img" aria-label="Pink and purple beads" style="background:linear-gradient(135deg,#e2a0d6,#9a4aa2)"></div>
  </div>

  <div class="join-rule"></div>
  <a class="join-banner" href="#">
    <span class="join-ask">Are you PSYCHIC?</span>
    <span class="join-now">Join Now
      <svg width="12" height="20" viewBox="0 0 12 20" aria-hidden="true"><path d="M2 2l8 8-8 8" fill="none" stroke="#1f5f85" stroke-width="2.5"/></svg>
    </span>
  </a>

  <div class="video-frame">
    <div class="video-still" role="img" aria-label="Video still of a woman speaking to camera"></div>
    <div class="video-bar"></div>
  </div>
  <div class="video-brand"><span class="brand-square"></span><span class="brand-word">Vidlume</span><span class="brand-label">Video</span></div>
  <h2 class="video-heading">How to be psychic, have intuition, and do mind reading</h2>
  <p class="video-text">Lorem Ipsum Proin gravida nibh vel velit auctor aliquet. Aenean sollicitudin, lorem quis bibendum auctor, nisi elit consequat ipsum, nec sagittis sem nibh id elit.</p>
  <a class="video-more" href="#">Read more »</a>

  <footer class="footer">
    <nav class="footer-links"><a href="#">About Us</a><a href="#">About Psychic Readings</a><a href="#">Contact Us</a><a href="#">Privacy Policy</a><a href="#">Terms &amp; Conditions</a></nav>
    <p class="footer-legal">© 2013 Lantern of Seers (ACN 000 123 456). Trademark Lantern of Seers</p>
  </footer>
</div>
</body>
</html>
```